Joomla Responsive Website Template for an International Biotechnology Company

Our client is a biotechnology company that uses silver-based technology to help make products antimicrobial, antibacterial, and anti fungal. We need a Joomla-based template that is responsive/mobile friendly when viewed on tablets or smartphones. We are looking for a template design for the home page and subpages. We are replacing the current website http://www.velmora-labs.com with a new website being built here: http://velmoraclean.com.stagehost.com/velmoraprime/. What we have now on the site is the basic wire frame. This is the desired layout and pictures we want to use. We would like you to add some design elements to make the website more professional looking and polished. Please refer to the attached style guide to help you in choosing the color. The client does like the green leaf, which is included in the last page of style guide and may be good for a background image. While the Velmora logo and leaf are green, we do not want to overuse the color green. The client does own other technologies that we will be promoting on the site and the logos for these technologies are attached below. These logos are Tusk, Velmora-Prime, and Wisp. We will be using this website to promote the technologies, the markets the technologies serve; drinking water, medical devices, apparel and textiles, and architectural surfaces, and to promote the customer using these devices. Please make the design "clean" and not cluttered, as these technologies are used to fight "dirty things".
Updates

Hello Designers! Thank you all very much for your design submissions. They were simply excellent. Due to the Holidays and New Years, many of the client's team members have been on vacation. We expect to have feedback shortly and pick the top design soon there after. Again, thank you all very much and hope the New Year brings you continued success. Best, Dorian

Industry/Entity Type

Biotechnology

Coding

Coded - Design and coding required

```html
<!DOCTYPE html>
<html lang="en">
<head>
<meta charset="utf-8">
<title>Velmora</title>
<link href="https://fonts.googleapis.com/css2?family=Open+Sans:wght@300;400;600;700&display=swap" rel="stylesheet">
<style>
:root{
  --green:#7cbd42;
  --green-dark:#6aa834;
  --green-line:#9ed06f;
  --ink:#3d3d3d;
  --muted:#666;
  --panel:#464646;
  --footer:#f2f2f2;
  --social:#2f6fb3;
  --white:#fff;
}
*{margin:0;padding:0;box-sizing:border-box}
html,body{width:748px;height:1200px;overflow:hidden}
body{position:relative;background:var(--white);font-family:"Open Sans",Arial,sans-serif;color:var(--ink)}
.abs{position:absolute}
.brand{left:70px;top:14px}
.brand-name{font-size:26px;font-weight:600;color:var(--green);letter-spacing:-0.5px;line-height:1}
.social{display:flex;gap:4px}
.social span{width:14px;height:14px;background:var(--social);border-radius:2px;display:block}
.header-social{left:646px;top:34px}
.nav{left:70px;top:56px;width:609px;height:32px;background:var(--green);display:flex;align-items:center}
.nav a{color:var(--white);text-decoration:none;font-size:7.5px;padding:0 9px;height:100%;display:flex;align-items:center;border-right:1px solid var(--green-line)}
.nav a.current{background:var(--green-dark)}
.search{margin-left:auto;margin-right:11px;width:122px;height:13px;background:var(--green-dark);color:var(--white);font-size:6px;padding-left:5px;display:flex;align-items:center}
.band{left:0;top:242px;width:748px;height:309px;background:var(--green)}
.hero{left:70px;top:88px;width:609px;height:246px;background:linear-gradient(180deg,#2b2e2f 0%,#4a4e50 45%,#eef0f0 62%,#ffffff 100%)}
.dots{left:626px;top:314px;display:flex;gap:5px}
.dots span{width:6px;height:6px;border-radius:50%;background:#555}
.dots span.on{background:var(--green)}
.market{width:140px;top:349px}
.market .photo{height:88px}
.market h3{font-size:7.5px;font-weight:700;color:var(--white);margin-top:20px}
.market p{font-size:6.6px;line-height:12.8px;color:#eaf5df;margin-top:6px}
.market .btn{display:inline-block;margin-top:9px;background:#5f8f36;color:var(--white);font-size:6px;padding:4px 6px}
.tech-title{left:70px;top:566px;font-size:21px;font-weight:400;color:var(--ink)}
.rule{left:70px;top:601px;width:349px;height:1px;background:#ddd}
.tech{left:78px;width:341px;display:flex}
.tech .mark{width:107px;font-size:22px;font-weight:700;letter-spacing:1px;padding-top:2px}
.tech p{font-size:6.8px;line-height:12.8px;color:var(--muted);width:226px}
.about{left:434px;top:551px;width:245px;height:219px;background:var(--panel);padding:20px 16px}
.about h2{font-size:19px;font-weight:400;color:var(--green)}
.about p{font-size:6.8px;line-height:12.8px;color:#e6e6e6;margin-top:10px}
.news{left:434px;top:770px;width:245px;height:342px;background:var(--green);padding:16px 18px}
.news h2{font-size:30px;font-weight:300;color:var(--white);line-height:1}
.news h2 small{display:block;font-size:19px;font-weight:600;margin-top:-2px}
.news-item{position:relative;padding-left:13px}
.news-item::before{content:"";position:absolute;left:0;top:5px;width:4px;height:4px;border-right:1.5px solid var(--white);border-bottom:1.5px solid var(--white);transform:rotate(-45deg)}
.news-item .date{font-size:12px;font-weight:300;color:var(--white)}
.news-item p{font-size:6.8px;line-height:12.8px;color:var(--white)}
.footer{left:0;top:1112px;width:748px;height:88px;background:var(--footer)}
.footer-links{left:68px;top:1143px;font-size:7.5px;color:var(--ink)}
.footer-links span{margin:0 7px}
.copy{left:68px;top:1166px;font-size:7px;color:var(--ink)}
.footer-social{left:646px;top:1154px}
</style>
</head>
<body>
<header>
  <div class="abs brand">
    <div class="brand-name">velmora</div>
  </div>
  <div class="abs social header-social" aria-label="Social links"><span></span><span></span></div>
  <nav class="abs nav">
    <a class="current">Home</a><a>About Us</a><a>Markets</a><a>Technology</a><a>Customer Programs</a><a>News Highlights</a><a>Contact Us</a>
    <div class="search">SEARCH</div>
  </nav>
</header>

<div class="abs band"></div>
<div class="abs hero" role="img" aria-label="Scientists in white lab suits working at microscopes before a chalkboard of chemical formulas"></div>
<div class="abs dots"><span class="on"></span><span></span><span></span><span></span></div>

<section>
  <div class="abs market" style="left:70px">
    <div class="photo" role="img" aria-label="Water pouring into a glass" style="background:linear-gradient(135deg,#1f5fae,#9cc6ee)"></div>
    <h3>Drinking Water</h3>
    <p>Lorem Ipsum is simply dummy text of the printing and typesetting industry. Lorem Ipsum has been the industry's .</p>
    <span class="btn">Read More</span>
  </div>
  <div class="abs market" style="left:226px">
    <div class="photo" role="img" aria-label="Surgical room with medical monitoring equipment" style="background:linear-gradient(135deg,#3e5466,#a9bccb)"></div>
    <h3>Medical Devices</h3>
    <p>Lorem Ipsum is simply dummy text of the printing and typesetting industry. Lorem Ipsum has been the industry's .</p>
    <span class="btn">Read More</span>
  </div>
  <div class="abs market" style="left:382px">
    <div class="photo" role="img" aria-label="Colourful shirts on hangers" style="background:linear-gradient(180deg,#f4f4f4 35%,#6a9a3c 60%,#c23a6e 100%)"></div>
    <h3>Textile &amp; Apparel</h3>
    <p>Lorem Ipsum is simply dummy text of the printing and typesetting industry. Lorem Ipsum has been the industry's .</p>
    <span class="btn">Read More</span>
  </div>
  <div class="abs market" style="left:538px">
    <div class="photo" role="img" aria-label="Curved modern building facade" style="background:linear-gradient(160deg,#2d5e8f,#d5e4f0)"></div>
    <h3>Architectural Surfaces</h3>
    <p>Lorem Ipsum is simply dummy text of the printing and typesetting industry. Lorem Ipsum has been the industry's .</p>
    <span class="btn">Read More</span>
  </div>
</section>

<section>
  <h2 class="abs tech-title">Technology</h2>
  <div class="abs rule"></div>
  <div class="abs tech" style="top:620px">
    <div class="mark" style="color:#1d1d1d">PRIME</div>
    <p>Velmora Prime represents the next generation of odor control for textiles and apparel. Velmora Prime is applied to textiles as a fabric finish creating gear and apparel that never smells! Designed to fit into the most demanding applications and environments – from performance and athletic apparel to sporting goods, home and commercial textiles and pet products, Velmora Prime stops odor and handles the toughest microbes to deliver unparalleled, long lasting freshness.</p>
  </div>
  <div class="abs tech" style="top:788px">
    <div class="mark" style="color:#1f6fb4">WISP</div>
    <p>Velmora Prime represents the next generation of odor control for textiles and apparel. Velmora Prime is applied to textiles as a fabric finish creating gear and apparel that never smells! Designed to fit into the most demanding applications and environments – from performance and athletic apparel to sporting goods, home and commercial textiles and pet products, Velmora Prime stops odor and handles the toughest microbes to deliver unparalleled, long lasting freshness.</p>
  </div>
  <div class="abs tech" style="top:962px">
    <div class="mark" style="color:#d9343a">TUSK</div>
    <p>Velmora Prime represents the next generation of odor control for textiles and apparel. Velmora Prime is applied to textiles as a fabric finish creating gear and apparel that never smells! Designed to fit into the most demanding applications and environments – from performance and athletic apparel to sporting goods, home and commercial textiles and pet products, Velmora Prime stops odor and handles the toughest microbes to deliver unparalleled, long lasting freshness.</p>
  </div>
</section>

<aside class="abs about">
  <h2>Velmora® Antimicrobial</h2>
  <p>Velmora branded antimicrobial technology makes products cleaner and longer lasting with silver, copper and zinc, which have been proven in use throughout history. Velmora antimicrobial technology provides built-in protection by working 24/7 resisting the growth of microbes. We work in close partnership with our customers, from development to end-user marketing, to deliver a product advantage that makes a real difference in the marketplace.</p>
  <p>*Velmora is an NRSB registered ionic silver technology and is not a nanosilver technology.</p>
</aside>

<aside class="abs news">
  <h2>News<small>&amp; Events</small></h2>
  <div class="news-item" style="margin-top:16px">
    <div class="date">9/3/2014</div>
    <p>Coastal Council of Clinical Hygiene (CCCH) Guidelines Include Velmora Antimicrobial-Treated Catheters(2)</p>
  </div>
  <div class="news-item" style="margin-top:32px">
    <div class="date">9/3/2014</div>
    <p>Coastal Council of Clinical Hygiene (CCCH) Guidelines Include Velmora Antimicrobial-Treated Catheters(2)</p>
  </div>
  <div class="news-item" style="margin-top:34px">
    <div class="date">9/3/2014</div>
    <p>Coastal Council of Clinical Hygiene (CCCH) Guidelines Include Velmora Antimicrobial-Treated Catheters(2)</p>
  </div>
</aside>

<footer>
  <div class="abs footer"></div>
  <div class="abs footer-links">Home<span>|</span>About Us<span>|</span>Markets<span>|</span>Technology<span>|</span>Customer Programs<span>|</span>News Highlights<span>|</span>Contact Us</div>
  <div class="abs copy">©2014 Company Name ,All Rights Reserved</div>
  <div class="abs social footer-social" aria-label="Social links"><span></span><span></span></div>
</footer>
</body>
</html>
```